50th Invite

Design a 50th birthday invite.

Key essentials to communicate are:

Date: 14 December 2019
Time: 7pm for 7.30pm departure
Birthday person: Glen
Theme: Boat Party
Location: Berth K4 27, Tidemoor

Other than that will leave to your creativity. Just for clarity, the above is info to be communicated somehow on the invite, I dont want it to be simply copied.

i would like a luxury boat theme, think Miami, Bahamas etc etc, photos or drawings OK

```html
<!DOCTYPE html>
<html lang="en">
<head>
<meta charset="utf-8">
<title>50th Birthday Invite</title>
<link rel="stylesheet" href="https://fonts.googleapis.com/css2?family=Jost:wght@200;300&display=swap">
<style>
  :root {
    --navy: #2b3a8f;
    --ocean: #0057a6;
    --sea: #0089d1;
    --lagoon: #00aeef;
    --silver-light: #d9dadd;
    --silver-mid: #a9acb2;
    --frond: #8dc63f;
    --frond-deep: #74b531;
    --ink: #ffffff;
    --page: #ffffff;
  }
  html, body {
    margin: 0;
    width: 1200px;
    height: 1200px;
    overflow: hidden;
    background: var(--page);
  }
  .invite {
    position: absolute;
    left: 191px;
    top: 32px;
    width: 816px;
    height: 1084px;
    overflow: hidden;
    background: linear-gradient(180deg, var(--navy) 0%, var(--ocean) 22%, var(--sea) 62%, var(--lagoon) 100%);
    font-family: "Jost", "Helvetica Neue", Arial, sans-serif;
  }
  .invite-art {
    position: absolute;
    inset: 0;
    width: 816px;
    height: 1084px;
  }
  .numeral {
    fill: none;
    stroke: url(#silver);
    stroke-width: 20;
  }
  .ordinal {
    font-family: "Jost", "Helvetica Neue", Arial, sans-serif;
    font-weight: 300;
    fill: var(--silver-mid);
  }
  .occasion {
    font-family: "Jost", "Helvetica Neue", Arial, sans-serif;
    font-weight: 300;
    fill: var(--ink);
  }
  .rule {
    stroke: var(--ink);
    stroke-width: 1.8;
  }
  .details {
    position: absolute;
    left: 69px;
    top: 657px;
    margin: 0;
    padding: 0;
    list-style: none;
    color: var(--ink);
    font-weight: 300;
    font-size: 43px;
    line-height: 49.6px;
    letter-spacing: 0.1em;
    white-space: nowrap;
  }
</style>
</head>
<body>
  <main class="invite">
    <svg class="invite-art" viewBox="0 0 816 1084" xmlns="http://www.w3.org/2000/svg">
      <defs>
        <linearGradient id="silver" gradientUnits="userSpaceOnUse" x1="100" y1="0" x2="700" y2="0">
          <stop offset="0" stop-color="var(--silver-light)"/>
          <stop offset="0.45" stop-color="var(--silver-mid)"/>
          <stop offset="1" stop-color="var(--silver-light)"/>
        </linearGradient>
        <linearGradient id="frond-fill" x1="0" y1="0" x2="1" y2="1">
          <stop offset="0" stop-color="var(--frond)"/>
          <stop offset="1" stop-color="var(--frond-deep)"/>
        </linearGradient>
      </defs>

      <circle role="img" aria-label="Palm fronds framed inside the zero" cx="533" cy="278" r="142"
              fill="url(#frond-fill)" opacity="0.6"/>

      <g role="img" aria-label="50">
        <path class="numeral" d="M393 90 L172 90 L155 232 C190 200 235 185 275 185 C335 185 374 230 374 282 C374 340 325 385 262 385 C185 385 130 350 103 310"/>
        <circle class="numeral" cx="533" cy="278" r="154"/>
      </g>
      <text class="ordinal" x="666" y="435" font-size="50">th</text>

      <path role="img" aria-label="Palm frond illustration" fill="url(#frond-fill)" opacity="0.9"
            d="M0 0 L230 0 C270 20 300 60 305 110 C240 100 170 120 110 152 C70 110 30 70 0 50 Z"/>

      <line class="rule" x1="112" y1="471" x2="722" y2="471"/>
      <text class="occasion" x="112" y="550" font-size="69"
            textLength="616" lengthAdjust="spacing">BIRTHDAY</text>
      <line class="rule" x1="114" y1="575" x2="726" y2="575"/>

      <path role="img" aria-label="Palm frond illustration" fill="url(#frond-fill)" opacity="0.9"
            d="M816 930 C740 940 640 960 518 990 C600 1020 680 1060 720 1084 L816 1084 Z"/>
    </svg>

    <ul class="details">
      <li>Date: 14 December 2019</li>
      <li>Time: 7pm for 7:30 departure</li>
      <li>Birthday Person:Glen</li>
      <li>Theme: Boat Party</li>
      <li>Location: Berth K4 27, Tidemoor</li>
    </ul>
  </main>
</body>
</html>
```